TRIVAN 2026 Flyer for Conference

TRIVAN needs a design for a 1-page flyer that we will hand out at an upcoming event & then later post online as a pdf. There are 3 elements which need to be on the flyer:

1) A logo. This should be prominent on the design (e.g., in the middle). The flyer should use the colors that are in that logo (e.g., for accents, design elements, and/or text; not all of these have to be used):
Dark blue: #185577
Med blue: #327C9A
Teal: #4EB1C2
Light Teal: #9EDBE6

2) The conference theme -- Forests of Wonder: Climbing toward Research Fluency -- should be at the flyer's top.

3) Finally, these six tracks should be listed below the theme and the logo (it's font size should be at least a couple sizes smaller than the size used for the theme):
- Pearls of Pedagogy: Teaching Techniques that Work
- The Depth Gauge: Measuring Instructional Impact
- Techtonic Shifts: Innovation and Educational Technology
- Captain's Log: Navigating Leadership in Library Instruction
- Swimming Together: Collaborating with Others
- The Bermuda Triangle: Exploring (Seemingly) Eternal Challenges

Font styles to use
Sans Serif

Colors
0094D4
00A9DD
6FCCEA
C7EBF8
E9F6FB

Requirements
Must have
• The 3 elements listed in the description: 1) the logo, 2) the text of the theme and 3) the text for the tracks.

```html
<!DOCTYPE html>
<html lang="en">
<head>
<meta charset="utf-8">
<title>TRIVAN 2026 – Forests of Wonder</title>
<link href="https://fonts.googleapis.com/css2?family=Poppins:wght@600;700&family=Urbanist:wght@400;500&display=swap" rel="stylesheet">
<style>
  :root {
    --deep: #185577;
    --mid: #327C9A;
    --teal: #4EB1C2;
    --light-teal: #9EDBE6;
    --track-title: #8ED3E0;
    --sky-top: #E9F6FB;
    --sky-bottom: #C7EBF8;
    --swell: #1D5E82;
    --white: #FFFFFF;
  }
  * { margin: 0; padding: 0; box-sizing: border-box; }
  html, body { width: 927px; height: 1200px; overflow: hidden; background: var(--deep); }
  .flyer {
    position: relative;
    width: 927px;
    height: 1200px;
    overflow: hidden;
    background: var(--deep);
    font-family: "Urbanist", sans-serif;
  }
  .sky {
    position: absolute;
    left: 0; top: 0;
    width: 927px; height: 480px;
    background: linear-gradient(180deg, var(--sky-top) 0%, var(--sky-bottom) 100%);
  }
  .sea {
    position: absolute;
    left: 0; top: 0;
    width: 927px; height: 1200px;
  }
  .art-whale {
    position: absolute;
    left: 285px; top: 100px;
    width: 425px; height: 205px;
    border-radius: 50%;
    background: radial-gradient(ellipse at center, rgba(78,177,194,0.55) 0%, rgba(78,177,194,0.25) 55%, rgba(158,219,230,0) 75%);
  }
  .art-wave {
    position: absolute;
    left: -20px; top: 250px;
    width: 225px; height: 140px;
    border-radius: 50%;
    background: radial-gradient(ellipse at center, rgba(78,177,194,0.55) 0%, rgba(158,219,230,0.2) 60%, rgba(158,219,230,0) 75%);
  }
  .art-seaweed {
    position: absolute;
    left: 450px; top: 300px;
    width: 150px; height: 170px;
    border-radius: 50%;
    background: radial-gradient(ellipse at center, rgba(50,124,154,0.45) 0%, rgba(50,124,154,0.15) 55%, rgba(50,124,154,0) 75%);
  }
  .brand {
    position: absolute;
    top: 28px;
    left: 0; width: 100%;
    display: flex;
    justify-content: center;
    align-items: center;
    gap: 14px;
  }
  .brand-dot {
    width: 52px; height: 52px;
    border-radius: 50%;
    background: var(--teal);
  }
  .brand-name {
    font-family: "Poppins", sans-serif;
    font-weight: 700;
    font-size: 48px;
    line-height: 1;
    letter-spacing: 0.5px;
    color: var(--deep);
  }
  .theme {
    position: absolute;
    top: 444px;
    left: 0; width: 100%;
    text-align: center;
    font-family: "Poppins", sans-serif;
    font-weight: 700;
    font-size: 57px;
    line-height: 92px;
    letter-spacing: -1.5px;
    color: var(--teal);
    -webkit-text-stroke: 6px var(--white);
    paint-order: stroke fill;
  }
  .tracks {
    position: absolute;
    top: 664px;
    left: 0; width: 100%;
    display: grid;
    grid-template-columns: 318px 290px 319px;
    row-gap: 28px;
  }
  .track {
    display: flex;
    flex-direction: column;
    align-items: center;
    text-align: center;
  }
  .track-icon {
    width: 91px; height: 91px;
    border-radius: 50%;
    background: var(--sky-top);
    display: flex;
    align-items: center;
    justify-content: center;
  }
  .track-icon svg {
    width: 54px; height: 54px;
    fill: none;
    stroke: var(--deep);
    stroke-width: 2;
    stroke-linecap: round;
    stroke-linejoin: round;
  }
  .track-name {
    margin-top: 12px;
    font-weight: 500;
    font-size: 22px;
    letter-spacing: -0.3px;
    color: var(--track-title);
  }
  .track-desc {
    margin-top: 10px;
    font-weight: 400;
    font-size: 17px;
    line-height: 27px;
    letter-spacing: -0.3px;
    color: var(--white);
    white-space: nowrap;
  }
  .track-desc.narrow { white-space: normal; max-width: 245px; }
  .social {
    position: absolute;
    top: 1133px;
    left: 0; width: 100%;
    display: flex;
    justify-content: center;
    align-items: center;
    gap: 7px;
  }
  .social-rule {
    width: 182px; height: 2px;
    background: var(--teal);
    margin: 0 12px;
  }
  .social-dot {
    width: 36px; height: 36px;
    border-radius: 50%;
    background: var(--white);
  }
</style>
</head>
<body>
<main class="flyer">
  <div class="sky"></div>
  <div class="art-whale" role="img" aria-label="Illustration of a smiling whale swimming among small fish"></div>
  <div class="art-wave" role="img" aria-label="Illustration of a curling ocean wave"></div>

  <svg class="sea" viewBox="0 0 927 1200" aria-hidden="true">
    <path fill="var(--deep)" d="M0,160 C40,175 58,220 66,290 C76,360 120,372 200,370 L450,374 C515,378 548,405 566,445 C600,405 660,385 720,368 C782,346 805,300 826,256 C852,212 885,200 927,205 L927,1200 L0,1200 Z"/>
    <path fill="var(--swell)" d="M927,690 C860,720 830,770 850,830 C870,900 900,960 927,980 Z"/>
    <path fill="var(--swell)" d="M0,1100 C80,1090 160,1120 230,1160 C260,1180 270,1200 270,1200 L0,1200 Z"/>
  </svg>

  <div class="art-seaweed" role="img" aria-label="Illustration of seaweed rising from the sea floor"></div>

  <header class="brand">
    <span class="brand-dot"></span>
    <span class="brand-name">TRIVAN 2026</span>
  </header>

  <h1 class="theme">Forests of Wonder: Climbing<br>toward Research Fluency</h1>

  <section class="tracks">
    <article class="track">
      <div class="track-icon">
        <svg viewBox="0 0 54 54"><rect x="6" y="6" width="42" height="28" rx="2"/><path d="M12 27 L20 19 L27 24 L38 13"/><path d="M18 34 V46 M36 34 V46 M12 46 H42"/></svg>
      </div>
      <h2 class="track-name">Pearls of Pedagogy</h2>
      <p class="track-desc">Teaching Techniques That Work</p>
    </article>
    <article class="track">
      <div class="track-icon">
        <svg viewBox="0 0 54 54"><path d="M8 46 H48"/><path d="M12 46 V38 M20 46 V32 M28 46 V34 M36 46 V26 M44 46 V20"/><path d="M10 34 L18 26 L26 30 L42 12"/><path d="M34 10 L44 8 L42 18 Z"/></svg>
      </div>
      <h2 class="track-name">Techtonic Shifts</h2>
      <p class="track-desc">Innovation and Educational Technology</p>
    </article>
    <article class="track">
      <div class="track-icon">
        <svg viewBox="0 0 54 54"><path d="M6 6 V48 H48 V6"/><path d="M10 16 q4 -3 8 0 M36 16 q4 -3 8 0 M10 28 q4 -3 8 0 M36 28 q4 -3 8 0 M10 40 q4 -3 8 0 M36 40 q4 -3 8 0"/><path d="M27 12 V42 M23 16 L27 12 L31 16 M23 38 L27 42 L31 38"/></svg>
      </div>
      <h2 class="track-name">The Depth Gauge</h2>
      <p class="track-desc">Measuring Instructional Impact</p>
    </article>
    <article class="track">
      <div class="track-icon">
        <svg viewBox="0 0 54 54"><circle cx="40" cy="22" r="6"/><path d="M6 34 q5 -4 10 0 q5 4 10 0 q5 -4 10 0 q5 4 10 0"/><path d="M6 42 q5 -4 10 0 q5 4 10 0 q5 -4 10 0 q5 4 10 0"/></svg>
      </div>
      <h2 class="track-name">Swimming Together</h2>
      <p class="track-desc">Collaborating with Others</p>
    </article>
    <article class="track">
      <div class="track-icon">
        <svg viewBox="0 0 54 54"><path d="M6 30 C6 18 16 12 27 12 C38 12 48 18 48 30 Z"/><path d="M10 30 H44 V38 C36 41 18 41 10 38 Z"/><path d="M27 17 V26 M23 20 H31 M23 24 q4 4 8 0"/></svg>
      </div>
      <h2 class="track-name">Captain's Log</h2>
      <p class="track-desc narrow">Navigating Leadership in Library Instruction</p>
    </article>
    <article class="track">
      <div class="track-icon">
        <svg viewBox="0 0 54 54"><circle cx="27" cy="10" r="5"/><circle cx="10" cy="42" r="5"/><circle cx="44" cy="42" r="5"/><path d="M24.5 14.5 L12.5 37.5 M29.5 14.5 L41.5 37.5 M15 42 H39"/></svg>
      </div>
      <h2 class="track-name">The Bermuda Triangle</h2>
      <p class="track-desc">Exploring Eternal Challenges</p>
    </article>
  </section>

  <footer class="social" aria-label="Social channels">
    <span class="social-rule"></span>
    <span class="social-dot"></span>
    <span class="social-dot"></span>
    <span class="social-dot"></span>
    <span class="social-rule"></span>
  </footer>
</main>
</body>
</html>
```